Header and Footer

Header : using the logo and the details of the villa and a photo + blurb (i will supply)

And Footer below with a Villa details plus a smaller logo, no writing on the same line

NO CURVES - all Straight lines - footer and header must be sent as separate components as jpgs

no colours other than the photo insertions and logo colours

Target Market(s)

upmarket Villa

Requirements
Must have
• Header must include all 3 photos and logo

Blurb below photos to read - The former Wheelwright Hall circa 1880. Restored beyond its former beauty by design with unsurpassed cutting edge luxury. Situated in the heart of the historic village of Ashvale in Kestrel Bay's breathtaking hinterland

Footer must include a smaller logo - no writing different from Header with our contact details.

48 Quarry Ridge Road | Ashvale Downs
www.hollowbrookmanor.com

0427958642
Should not have
• anything than described

```html
<!DOCTYPE html>
<html lang="en">
<head>
<meta charset="utf-8">
<title>Hollowbrook Manor – Letterhead</title>
<link href="https://fonts.googleapis.com/css2?family=EB+Garamond:ital,wght@0,400;0,600;1,400&display=swap" rel="stylesheet">
<style>
  :root {
    --charcoal: #333333;
    --charcoal-deep: #2a2a2a;
    --paper: #ffffff;
    --ink-light: #f2f2f2;
    --mark-grey: #8d8d8d;
    --accent-red: #e8412b;
    --photo-sky: #6f95c4;
    --photo-shade: #4a5058;
    --photo-room: #b8613c;
  }
  * { margin: 0; padding: 0; box-sizing: border-box; }
  html, body { width: 849px; height: 1200px; overflow: hidden; background: var(--paper); }
  .sheet { position: relative; width: 849px; height: 1200px; background: var(--paper); font-family: 'EB Garamond', Georgia, serif; }

  .masthead { position: absolute; left: 0; top: 0; width: 849px; height: 178px; background: var(--charcoal); }
  .masthead-shadow { position: absolute; left: 0; top: 178px; width: 849px; height: 20px;
    background: linear-gradient(to bottom, var(--charcoal-deep), #3b3b3b 60%, #5a5a5a); }

  .brand { position: absolute; display: flex; align-items: center; gap: 10px; color: var(--mark-grey); font-weight: 600; text-transform: uppercase; white-space: nowrap; }
  .brand-square { background: var(--accent-red); flex: none; }
  .brand--large { left: 40px; top: 52px; font-size: 38px; letter-spacing: 2px; }
  .brand--large .brand-square { width: 18px; height: 18px; }
  .brand--small { left: 36px; top: 1101px; font-size: 17px; letter-spacing: 1px; }
  .brand--small .brand-square { width: 10px; height: 10px; }

  .blurb { position: absolute; left: 414px; top: 37px; width: 388px; color: var(--ink-light);
    font-style: italic; font-size: 17.4px; line-height: 22.5px; letter-spacing: 0.2px;
    text-align: justify; text-align-last: left; }

  .footer-shadow { position: absolute; left: 0; top: 1032px; width: 849px; height: 20px;
    background: linear-gradient(to bottom, #404040, var(--charcoal-deep)); }
  .footer { position: absolute; left: 0; top: 1052px; width: 849px; height: 148px; background: var(--charcoal); }

  .gallery { position: absolute; left: 235px; top: 1081px; display: flex; height: 87px; }
  .gallery-photo { width: 125px; height: 87px; }
  .gallery-photo--exterior { background: linear-gradient(to bottom, var(--photo-sky), #9ab6d6 55%, #7a7466); }
  .gallery-photo--veranda { background: linear-gradient(to bottom, #6e86a4, var(--photo-shade) 50%, #8a6a48); }
  .gallery-photo--interior { background: linear-gradient(to right, #d9d6cf, var(--photo-room) 75%, #d98a3c); }

  .contact { position: absolute; right: 33px; top: 1111px; color: var(--ink-light); font-size: 13.6px; line-height: 14.5px; text-align: right; font-style: normal; }
</style>
</head>
<body>
<div class="sheet">
  <header class="masthead">
    <div class="brand brand--large"><span class="brand-square"></span>Hollowbrook</div>
    <p class="blurb">The former Wheelwright Hall circa 1880. Restored beyond its former beauty by design with unsurpassed cutting edge luxury. Situated in the heart of the historic village of Ashvale in Kestrel Bay’s breathtaking hinterland.</p>
  </header>
  <div class="masthead-shadow"></div>

  <div class="footer-shadow"></div>
  <footer class="footer"></footer>
  <div class="brand brand--small"><span class="brand-square"></span>Hollowbrook</div>
  <div class="gallery">
    <div class="gallery-photo gallery-photo--exterior" role="img" aria-label="Photo of the restored hall exterior with white picket fence under blue sky"></div>
    <div class="gallery-photo gallery-photo--veranda" role="img" aria-label="Photo of the veranda with white lounge chairs and garden"></div>
    <div class="gallery-photo gallery-photo--interior" role="img" aria-label="Photo of the open-plan dining room with red feature wall"></div>
  </div>
  <address class="contact">
    48 Quarry Ridge Road<br>
    Ashvale Downs<br>
    www.hollowbrookmanor.com<br>
    0427958642
  </address>
</div>
</body>
</html>
```